Short term Rentals Marketing agency needs Web design.

We Need a web design for our new company based in Calgary, AB. We are a International Luxury home sharing company (short term rental properties, Villas, Boutique Hotels, Bed & Breakfast, Realtors, Mortgage Brokers). We would like to see designs that look simple, modern and professional. Colors would be bold (red, black, white). The final design should communicate something welcoming, symbolize innovation, and growth. Our goal is to form partnerships with Real Estate, Property Management, Short term Rental Clients to make their lives easier and increase revenue. Vlto Harbor Co. offers a flexible and secure way to market our clients properties while maintaining client satisfaction and amazing customer service. We like how https://plumtrellisads.ca/ is interactive (when you scroll down, text gets larger). Other similar websites for Short Term Rentals is https://www.thekeyhavenfirm.com/, https://stayvorabnb.com/, https://www.nestquill.com/, https://www.roostfinch.com/about-us/, https://lodgewardens.com. We have attached our Logo.

Target Market(s)

short term rental properties, Villas, Boutique Hotels, Bed & Breakfast, Realtors, Mortgage Brokers, property owners

Industry/Entity Type

Real Estate

Coding

Coded - Design and coding required

Number of Pages Required

5+ page

Font styles to use
Sans Serif

Requirements
Must have
• Home Page, About Us page, How it works, Services, Contact us.

We like how https://plumtrellisads.ca/ is interactive (when you scroll down, text gets larger).

We have attached our Webcopy. We would like Call to Action Buttons where they're located in the copy and page.

Must have our Logo Colors.

Other similar websites for Short Term Rentals is https://www.thekeyhavenfirm.com/, https://stayvorabnb.com/, https://www.nestquill.com/, https://www.roostfinch.com/about-us/, https://lodgewardens.com.
Nice to have
• Catchy, Interactive Home page.

Should not have
• Should not be too cluttered

```html
<!DOCTYPE html>
<html lang="en">
<head>
<meta charset="UTF-8">
<title>Vlto Harbor Co. – Short-Term Rental Marketing</title>
<link href="https://fonts.googleapis.com/css2?family=Montserrat:wght@500;600;700;800&family=Open+Sans:wght@400;600;700&display=swap" rel="stylesheet">
<style>
:root{
  --red:#e3262b;
  --red-dark:#c81d22;
  --ink:#1c1c1c;
  --charcoal:#242424;
  --text:#3a3a3a;
  --muted:#6c6c6c;
  --line:#dedede;
  --paper:#ffffff;
  --soft:#f4f4f4;
}
*{margin:0;padding:0;box-sizing:border-box}
html,body{width:1200px;height:4248px;overflow:hidden}
body{font-family:"Open Sans",Arial,sans-serif;color:var(--text);background:var(--paper);position:relative}
h1,h2,h3,h4,.btn,.nav a,.brand{font-family:"Montserrat",Arial,sans-serif}
.btn{display:inline-block;font-size:13px;font-weight:700;letter-spacing:.5px;text-transform:uppercase;padding:12px 20px;color:#fff;background:var(--red);border-radius:2px;text-decoration:none}
.btn--dark{background:var(--ink)}
.btn--light{background:#fff;color:var(--ink)}

/* header */
.site-header{height:104px;display:flex;align-items:center;padding:0 90px 0 96px;background:#fff;box-shadow:0 2px 8px rgba(0,0,0,.06);position:relative;z-index:2}
.brand{display:flex;align-items:center;gap:10px;font-size:24px;font-weight:800;color:var(--ink);text-decoration:none;width:306px}
.brand-mark{width:22px;height:22px;background:var(--red)}
.nav{display:flex;gap:30px;margin-right:auto}
.nav a{font-size:14px;font-weight:500;color:var(--ink);text-decoration:none;padding-bottom:6px}
.nav a.is-active{color:var(--red);border-bottom:2px solid var(--red)}
.site-header .btn{font-size:14px;padding:14px 18px}

/* hero */
.hero{height:616px;position:relative;display:flex;flex-direction:column;align-items:center;justify-content:center;text-align:center}
.hero-photo{position:absolute;inset:0;background:linear-gradient(180deg,#d9d4cc 0%,#cbbfae 45%,#8c7a66 75%,#5d4c3d 100%)}
.hero-photo::after{content:"";position:absolute;inset:0;background:rgba(0,0,0,.22)}
.hero-content{position:relative;z-index:1}
.hero h1{font-size:44px;font-weight:800;color:#fff;line-height:1.25;max-width:760px;text-shadow:2px 2px 0 var(--red)}
.hero .btn{margin-top:28px;padding:14px 26px}
.hero-dots{position:absolute;bottom:26px;left:50%;transform:translateX(-50%);display:flex;gap:8px;z-index:1}
.hero-dots span{width:10px;height:10px;border-radius:50%;background:rgba(255,255,255,.55)}
.hero-dots span.is-current{background:var(--red)}

/* welcome */
.welcome{height:480px;padding:70px 150px 0;text-align:center}
.welcome h2{font-size:36px;font-weight:800;color:var(--ink)}
.welcome h2 span{color:var(--red)}
.welcome p{margin-top:30px;font-size:14.5px;line-height:1.95}
.btn-row{margin-top:30px;display:flex;justify-content:center;gap:12px}

/* about */
.about{height:720px;position:relative;background:var(--charcoal);display:flex;align-items:center}
.about-edges{position:absolute;inset:0;width:100%;height:100%}
.about-photo{position:absolute;left:0;top:60px;width:540px;height:600px;background:linear-gradient(135deg,#efe9e1 0%,#c9b7a2 55%,#8e7761 100%)}
.about-text{position:relative;margin-left:580px;width:520px;color:#fff}
.about-text h2{font-size:42px;font-weight:800}
.about-text p{margin-top:26px;font-size:15px;line-height:2}
.about-text .btn{margin-top:30px}

/* features */
.features{height:600px;display:flex;justify-content:center;gap:40px;padding-top:60px}
.feature-card{width:328px;height:528px;border:1px solid var(--line);box-shadow:0 3px 10px rgba(0,0,0,.08);text-align:center;padding:12px 12px 0;background:#fff}
.feature-photo{height:190px}
.feature-card h3{margin-top:28px;font-size:17px;font-weight:800;color:var(--ink);line-height:1.35}
.feature-card p{margin-top:14px;font-size:14px;line-height:1.85;padding:0 14px}
.feature-card .btn{margin-top:20px}

/* how it works */
.how{height:820px;position:relative;text-align:center;color:#fff}
.how-bg{position:absolute;inset:0;width:100%;height:100%}
.how-inner{position:relative;padding-top:120px}
.how h2{font-size:42px;font-weight:800}
.how-intro{margin:22px auto 0;width:690px;font-size:15px;line-height:1.9}
.steps{display:flex;justify-content:center;gap:80px;margin-top:54px}
.step{width:300px}
.step-icon{width:110px;height:110px;margin:0 auto}
.step h3{margin-top:24px;font-size:20px;font-weight:600}
.step p{margin-top:14px;font-size:13px;line-height:1.9}
.how .btn{margin-top:54px;padding:14px 22px}

/* testimonials */
.reviews{height:390px;text-align:center;position:relative;padding-top:46px}
.reviews h2{font-size:30px;font-weight:800;color:var(--ink)}
.review-list{display:flex;justify-content:center;gap:60px;margin-top:40px}
.review{width:440px;height:196px;border:1px solid var(--line);box-shadow:0 3px 10px rgba(0,0,0,.08);display:flex;align-items:center;gap:28px;padding:0 30px;text-align:left;border-radius:2px}
.review-avatar{width:88px;height:88px;border-radius:50%;flex:none;border:3px solid #fff;box-shadow:0 0 0 2px var(--line)}
.stars{display:flex;gap:4px}
.review p{margin-top:10px;font-size:13px;line-height:1.7}
.review cite{display:block;margin-top:10px;font-size:13px;font-style:italic;color:var(--ink)}
.slider-arrow{position:absolute;top:218px;width:42px;height:42px;border-radius:50%;background:#c9c9c9;display:flex;align-items:center;justify-content:center}
.slider-arrow.prev{left:36px}
.slider-arrow.next{right:36px}

/* footer */
.site-footer{position:absolute;left:0;top:3786px;width:1200px;height:462px;background:var(--ink);color:#fff;border-top:6px solid var(--red)}
.footer-cols{display:flex;padding:70px 90px 0 96px}
.footer-brand{width:290px}
.footer-brand .brand{color:#fff;font-size:26px}
.footer-brand p{margin-top:22px;font-size:14px;line-height:1.75}
.socials{display:flex;gap:12px;margin-top:22px}
.socials span{width:34px;height:34px;border-radius:50%;border:2px solid #fff}
.footer-col{width:380px}
.footer-col h4{font-size:17px;font-weight:700;color:var(--red);text-transform:uppercase}
.contact-list{list-style:none;margin-top:26px}
.contact-list li{display:flex;align-items:center;gap:16px;font-size:14px;line-height:1.6;margin-bottom:18px}
.contact-icon{width:34px;height:34px;border-radius:50%;background:var(--red);display:flex;align-items:center;justify-content:center;flex:none}
.newsletter p{margin-top:20px;font-size:14px}
.subscribe{display:flex;margin-top:18px}
.subscribe span{width:270px;height:50px;background:#fff;color:var(--muted);font-size:14px;display:flex;align-items:center;padding-left:16px}
.subscribe i{width:50px;height:50px;background:var(--red);display:flex;align-items:center;justify-content:center}
.footer-bottom{position:absolute;bottom:0;left:0;right:0;height:48px;border-top:1px solid #3a3a3a;display:flex;align-items:center;justify-content:center;font-size:12px;color:#bdbdbd}
</style>
</head>
<body>

<header class="site-header">
  <a class="brand" href="#"><span class="brand-mark"></span>Vlto Harbor Co.</a>
  <nav class="nav">
    <a href="#" class="is-active">Home</a>
    <a href="#">About Us</a>
    <a href="#">How it works</a>
    <a href="#">Services</a>
    <a href="#">Contact us</a>
  </nav>
  <a class="btn" href="#">Request Consultation</a>
</header>

<section class="hero">
  <div class="hero-photo" role="img" aria-label="Bright modern living room with sofa, framed art and wooden sideboard"></div>
  <div class="hero-content">
    <h1>Partner With Us and Let's Start Growing Together!</h1>
    <a class="btn" href="#">Work With Us</a>
  </div>
  <div class="hero-dots"><span class="is-current"></span><span></span><span></span></div>
</section>

<section class="welcome">
  <h2>WELCOME TO <span>VLTO HARBOR CO</span></h2>
  <p>Vlto Harbor Co. is here to manage and market your short-term rental properties so you don't have to. Enjoy peace of mind in knowing your short-term rental properties, vacation homes, villas, hotels, and B&amp;Bs are safe, secure, and profitable – no matter where you are in the world. We will help you market, manage, and capitalize on everything, from your newest bookings to house cleaning and upkeep. Vlto Harbor Co. saves you time, money, and effort, so that you can focus on the things that matter most to you. Let us help you increase your rental revenue in a simple and hassle-free way by increasing your occupancy, streamlining your bookings, getting you amazing exposure, and more.</p>
  <div class="btn-row">
    <a class="btn" href="#">Read More</a>
    <a class="btn btn--dark" href="#">Contact Us</a>
  </div>
</section>

<section class="about">
  <svg class="about-edges" viewBox="0 0 1200 720" preserveAspectRatio="none" aria-hidden="true">
    <polygon points="0,0 1200,0 1200,40 0,0" fill="#fff"/>
    <polygon points="0,0 1200,40 1200,52 0,8" fill="var(--red)"/>
    <polygon points="0,720 1200,720 0,680" fill="#fff"/>
    <polygon points="0,668 1200,708 1200,720 0,680" fill="var(--red)"/>
  </svg>
  <div class="about-photo" role="img" aria-label="Family carrying moving boxes into a sunlit home"></div>
  <div class="about-text">
    <h2>ABOUT US</h2>
    <p>Vlto Harbor Co. offers you a flexible and secure way to oversee and manage and market your short-term rental properties. We have the skills needed to get our clients the absolute best value for their money, because we give our 110% to each and every one of our valued property owners. Some of the things that set us apart include:</p>
    <a class="btn" href="#">Read More</a>
  </div>
</section>

<section class="features">
  <article class="feature-card">
    <div class="feature-photo" role="img" aria-label="Host handing house keys to a guest" style="background:linear-gradient(135deg,#f3ece6,#d8c1b0 60%,#b08d78)"></div>
    <h3>INCREASE YOUR<br>REVENUE</h3>
    <p>Having Vlto Harbor Co. manage and market your rental property lets you benefit from increased revenues without having to put in the hours of work yourself. Vlto Harbor Co. will</p>
    <a class="btn" href="#">Read More</a>
  </article>
  <article class="feature-card">
    <div class="feature-photo" role="img" aria-label="Wooden staircase inside a modern home" style="background:linear-gradient(135deg,#e9e3dc,#b9a58f 55%,#6f5a47)"></div>
    <h3>RECEIVE CONSTANT<br>SUPPORT</h3>
    <p>Our dedicated team is there to take care of your property so that you don't have to. Our affordable and professional services include being there to support your guests, constant technical</p>
    <a class="btn" href="#">Read More</a>
  </article>
  <article class="feature-card">
    <div class="feature-photo" role="img" aria-label="Row of suburban houses under a blue sky" style="background:linear-gradient(180deg,#9fc3e3,#d7dde2 50%,#7d8a6e)"></div>
    <h3>MANAGE YOUR RISKS AND<br>INSURANCE</h3>
    <p>Having Vlto Harbor Co. manage and market your rental property lets you benefit from increased revenues without having to put in the hours of work yourself. Vlto Harbor Co. will</p>
    <a class="btn" href="#">Read More</a>
  </article>
</section>

<section class="how">
  <svg class="how-bg" viewBox="0 0 1200 820" preserveAspectRatio="none" role="img" aria-label="Red-tinted row of townhouses behind the steps">
    <defs>
      <linearGradient id="howTint" x1="0" y1="0" x2="0" y2="1">
        <stop offset="0" stop-color="#e8383c"/>
        <stop offset="1" stop-color="#d8262b"/>
      </linearGradient>
    </defs>
    <polygon points="0,40 1200,0 1200,820 0,820" fill="url(#howTint)"/>
  </svg>
  <div class="how-inner">
    <h2>HOW IT WORKS</h2>
    <p class="how-intro">We try to keep our application, management, and marketing process as quick and simple as possible. To sign up to Vlto Harbor Co. you can follow these three steps:</p>
    <div class="steps">
      <div class="step">
        <svg class="step-icon" viewBox="0 0 110 110" aria-hidden="true">
          <polygon points="55,4 99,29 99,81 55,106 11,81 11,29" fill="var(--ink)" stroke="#fff" stroke-width="3"/>
          <rect x="36" y="38" width="38" height="34" rx="2" fill="none" stroke="#fff" stroke-width="3"/>
          <line x1="36" y1="48" x2="74" y2="48" stroke="#fff" stroke-width="3"/>
          <line x1="45" y1="32" x2="45" y2="42" stroke="#fff" stroke-width="3"/>
          <line x1="65" y1="32" x2="65" y2="42" stroke="#fff" stroke-width="3"/>
          <polyline points="46,60 53,66 65,55" fill="none" stroke="#fff" stroke-width="3"/>
        </svg>
        <h3>Book A Consultation</h3>
        <p>Give us a call to set up your consultation session where we will discuss your needs, goals and concerns regarding the management and marketing of your short-term rental properties.</p>
      </div>
      <div class="step">
        <svg class="step-icon" viewBox="0 0 110 110" aria-hidden="true">
          <polygon points="55,4 99,29 99,81 55,106 11,81 11,29" fill="var(--ink)" stroke="#fff" stroke-width="3"/>
          <polyline points="34,56 52,40 70,56" fill="none" stroke="#fff" stroke-width="3"/>
          <polyline points="39,52 39,72 60,72" fill="none" stroke="#fff" stroke-width="3"/>
          <circle cx="63" cy="62" r="8" fill="none" stroke="#fff" stroke-width="3"/>
          <line x1="69" y1="68" x2="77" y2="76" stroke="#fff" stroke-width="3"/>
        </svg>
        <h3>Optimize Your Property</h3>
        <p>Once you've decided what you would like from your rental property, we will help you make it a reality. This involves optimizing your pricing, listings, calendars, bookings, and much more.</p>
      </div>
      <div class="step">
        <svg class="step-icon" viewBox="0 0 110 110" aria-hidden="true">
          <polygon points="55,4 99,29 99,81 55,106 11,81 11,29" fill="var(--ink)" stroke="#fff" stroke-width="3"/>
          <polyline points="33,56 55,36 77,56" fill="none" stroke="#fff" stroke-width="3"/>
          <polyline points="39,51 39,74 71,74 71,51" fill="none" stroke="#fff" stroke-width="3"/>
          <rect x="49" y="58" width="12" height="16" fill="none" stroke="#fff" stroke-width="3"/>
        </svg>
        <h3>Start Hosting Renters</h3>
        <p>You can start hosting renters in no time thanks to our quick turnaround times and professional services. We will help you maintain your property for as long as you need us.</p>
      </div>
    </div>
    <a class="btn btn--light" href="#">Get Started Today</a>
  </div>
</section>

<section class="reviews">
  <h2>WHAT PEOPLE ARE SAYING ABOUT VLTO HARBOR CO</h2>
  <div class="review-list">
    <figure class="review">
      <div class="review-avatar" role="img" aria-label="Client portrait" style="background:linear-gradient(135deg,#d9dee4,#9aa6b2)"></div>
      <div>
        <div class="stars">
          <svg width="16" height="16" viewBox="0 0 24 24"><polygon points="12,2 15,9 22,9 16.5,14 18.5,21 12,17 5.5,21 7.5,14 2,9 9,9" fill="#f5b400"/></svg>
          <svg width="16" height="16" viewBox="0 0 24 24"><polygon points="12,2 15,9 22,9 16.5,14 18.5,21 12,17 5.5,21 7.5,14 2,9 9,9" fill="#f5b400"/></svg>
          <svg width="16" height="16" viewBox="0 0 24 24"><polygon points="12,2 15,9 22,9 16.5,14 18.5,21 12,17 5.5,21 7.5,14 2,9 9,9" fill="#f5b400"/></svg>
          <svg width="16" height="16" viewBox="0 0 24 24"><polygon points="12,2 15,9 22,9 16.5,14 18.5,21 12,17 5.5,21 7.5,14 2,9 9,9" fill="#f5b400"/></svg>
          <svg width="16" height="16" viewBox="0 0 24 24"><polygon points="12,2 15,9 22,9 16.5,14 18.5,21 12,17 5.5,21 7.5,14 2,9 9,9" fill="#f5b400"/></svg>
        </div>
        <p>Lorem Ipsum is simply dummy text of the printing and typesetting industry. Lorem Ipsum has been</p>
        <cite>-Client Name</cite>
      </div>
    </figure>
    <figure class="review">
      <div class="review-avatar" role="img" aria-label="Client portrait" style="background:linear-gradient(135deg,#e6dcd5,#a8948a)"></div>
      <div>
        <div class="stars">
          <svg width="16" height="16" viewBox="0 0 24 24"><polygon points="12,2 15,9 22,9 16.5,14 18.5,21 12,17 5.5,21 7.5,14 2,9 9,9" fill="#f5b400"/></svg>
          <svg width="16" height="16" viewBox="0 0 24 24"><polygon points="12,2 15,9 22,9 16.5,14 18.5,21 12,17 5.5,21 7.5,14 2,9 9,9" fill="#f5b400"/></svg>
          <svg width="16" height="16" viewBox="0 0 24 24"><polygon points="12,2 15,9 22,9 16.5,14 18.5,21 12,17 5.5,21 7.5,14 2,9 9,9" fill="#f5b400"/></svg>
          <svg width="16" height="16" viewBox="0 0 24 24"><polygon points="12,2 15,9 22,9 16.5,14 18.5,21 12,17 5.5,21 7.5,14 2,9 9,9" fill="#f5b400"/></svg>
          <svg width="16" height="16" viewBox="0 0 24 24"><polygon points="12,2 15,9 22,9 16.5,14 18.5,21 12,17 5.5,21 7.5,14 2,9 9,9" fill="#f5b400"/></svg>
        </div>
        <p>Lorem Ipsum is simply dummy text of the printing and typesetting industry. Lorem Ipsum has been</p>
        <cite>-Client Name</cite>
      </div>
    </figure>
  </div>
  <span class="slider-arrow prev"><svg width="14" height="14" viewBox="0 0 14 14"><polyline points="9,2 4,7 9,12" fill="none" stroke="#fff" stroke-width="2.5"/></svg></span>
  <span class="slider-arrow next"><svg width="14" height="14" viewBox="0 0 14 14"><polyline points="5,2 10,7 5,12" fill="none" stroke="#fff" stroke-width="2.5"/></svg></span>
</section>

<footer class="site-footer">
  <div class="footer-cols">
    <div class="footer-brand">
      <a class="brand" href="#"><span class="brand-mark"></span>Vlto Harbor Co.</a>
      <p>Lorem ipsum dolor sit amet, consectetur adipiscing elit, sed do eiusmod tempor incididunt</p>
      <div class="socials"><span></span><span></span><span></span></div>
    </div>
    <div class="footer-col">
      <h4>Contact Us</h4>
      <ul class="contact-list">
        <li><span class="contact-icon"><svg width="16" height="16" viewBox="0 0 24 24"><path d="M12 2a7 7 0 0 0-7 7c0 5 7 13 7 13s7-8 7-13a7 7 0 0 0-7-7zm0 9.5A2.5 2.5 0 1 1 12 6.5a2.5 2.5 0 0 1 0 5z" fill="#fff"/></svg></span>480 Coral Reef Avenue<br>Suite 1200 Miami, Florida 33131</li>
        <li><span class="contact-icon"><svg width="15" height="15" viewBox="0 0 24 24"><path d="M6.6 10.8a15 15 0 0 0 6.6 6.6l2.2-2.2a1 1 0 0 1 1-.25 11.4 11.4 0 0 0 3.6.57 1 1 0 0 1 1 1V20a1 1 0 0 1-1 1A17 17 0 0 1 3 4a1 1 0 0 1 1-1h3.5a1 1 0 0 1 1 1c0 1.25.2 2.45.57 3.57a1 1 0 0 1-.25 1z" fill="#fff"/></svg></span>(888) 555-0142</li>
        <li><span class="contact-icon"><svg width="16" height="16" viewBox="0 0 24 24"><rect x="3" y="5" width="18" height="14" rx="1.5" fill="none" stroke="#fff" stroke-width="2"/><polyline points="3,6 12,13 21,6" fill="none" stroke="#fff" stroke-width="2"/></svg></span>info@VltoHarbor.Co</li>
      </ul>
    </div>
    <div class="footer-col newsletter">
      <h4>Subscribe to Newsletter</h4>
      <p>Lorem ipsum dolor sit amet, consectetur</p>
      <div class="subscribe">
        <span>Enter Your Email</span>
        <i><svg width="18" height="18" viewBox="0 0 24 24"><polygon points="2,21 23,12 2,3 2,10 17,12 2,14" fill="#fff"/></svg></i>
      </div>
    </div>
  </div>
  <div class="footer-bottom">© 2024 All Rights Reserved | Privacy Policy | Terms and Conditions | Disclaimer</div>
</footer>

</body>
</html>
```